Tea box package for Herbal Teas

We would like a design for a package of our tea products. We want the consumer to understand that our products are natural just by looking at the package. We prefer minimalistic designs.
The package we want would be a square (or slightly rectangular) box. The box would be generic enough for us to use it for different teas. Essentially what we want is all the main information and designs to be the same for each tea product we have. We would like to be able to change the main color and the name of the tea then to customize to the tea in the package. Please see the attached images for examples.
We really like the package in tea_packaging_example_4 picture. We would like our packaging to be something very similar but with all the labels printed on the package.
We already have our logo so I am attaching that as well (image named 'velka brin logo copy'). That would go on the front of the box.
We also attach a tile created using our logo (see image called 'tile'). We would like this to go to the sides similarly to tea_packaging_example_4.
On the back of the pouch, we want to have directions on how to make the tea but we want this section to be editable. For now just 3-4 lines of sample text is fine along with instructions on how to make a tea, see picture 'back of tea box'.
We would like for the box color to be as in example picture
tea_packaging_example_4. The color of the writing should be the same as the logo color. The font style should be something that would look nice next to the logo font, we are not sure what that font should be. The only thing colored would be the name of the tea and the ribbon as seen in tea_packaging_example_4, which we would like to change if we need to, to other variations.
Thanks a lot. For any questions, please contact me.

```html
<!DOCTYPE html>
<html lang="en">
<head>
<meta charset="utf-8">
<title>Ceylon Black Tea – Box Panels</title>
<link rel="stylesheet" href="https://fonts.googleapis.com/css2?family=Barlow:wght@400;600;700&family=Montserrat:wght@600&display=swap">
<style>
  :root {
    --page: #ffffff;
    --kraft: #d2ad83;
    --kraft-deep: #b89670;
    --kraft-faint: #c4a27a;
    --ink: #3a3a3a;
    --ink-soft: #4a4644;
    --ribbon: #ee7d1a;
    --gold-a: #b78a2d;
    --gold-b: #f6dd8a;
    --gold-c: #a57a22;
    --paper: #ffffff;
  }
  * { box-sizing: border-box; margin: 0; padding: 0; }
  html, body { width: 1000px; height: 1200px; overflow: hidden; background: var(--page); }
  body { position: relative; font-family: "Barlow", Arial, sans-serif; color: var(--ink); }

  .panel {
    position: absolute; width: 470px; height: 470px;
    background: var(--kraft); overflow: hidden;
    border: 3px solid var(--ink);
  }
  .panel::after {
    content: ""; position: absolute; inset: 9px;
    border: 2px solid var(--ink); pointer-events: none; z-index: 5;
  }
  .panel--side  { left: 23px;  top: 123px; }
  .panel--lid   { left: 507px; top: 123px; }
  .panel--back  { left: 23px;  top: 607px; }
  .panel--front { left: 507px; top: 607px; }

  .tile-area {
    position: absolute; left: 24px; top: 24px; right: 24px; bottom: 24px;
    border-radius: 4px;
    background: linear-gradient(160deg, #8b7660 0%, #746352 50%, #8b7660 100%);
  }

  .ornament-faint {
    position: absolute; left: 45px; top: 90px; width: 380px; height: 354px;
    border-radius: 50%;
    background: radial-gradient(ellipse at center, var(--kraft-faint) 0%, var(--kraft-deep) 100%);
    opacity: .75;
  }
  .ornament-dark {
    position: absolute; left: 45px; top: 73px; width: 380px; height: 354px;
    border-radius: 50%;
    background: radial-gradient(ellipse at center, var(--ink-soft) 0%, var(--ink) 70%);
  }
  .ornament-frame {
    position: absolute; left: 24px; top: 24px; right: 24px; bottom: 24px;
    border-radius: 10px;
    background: linear-gradient(160deg, #7d6a56, #665746);
  }

  .ribbon {
    position: absolute; left: 145px; width: 177px; top: 0;
    background: linear-gradient(90deg, var(--gold-c), var(--gold-b) 45%, var(--gold-a));
    padding: 0 9px;
  }
  .ribbon__body { height: 100%; background: var(--ribbon); position: relative; }
  .ribbon--full { height: 470px; }
  .ribbon--pointed { height: 303px; clip-path: polygon(0 0,100% 0,100% 88%,50% 100%,0 88%); }
  .ribbon--pointed .ribbon__body { height: 96%; clip-path: polygon(0 0,100% 0,100% 88%,50% 100%,0 88%); }

  .brand-disc {
    position: absolute; left: 50%; width: 122px; height: 122px; margin-left: -61px;
    border-radius: 50%; background: var(--paper);
    display: flex; align-items: center; justify-content: center;
  }
  .brand-name { font-weight: 600; font-size: 13px; letter-spacing: 1px; color: var(--ink); text-transform: uppercase; }

  .tea-name { position: absolute; left: 0; right: 0; text-align: center; font-family: "Montserrat", Arial, sans-serif; font-weight: 600; color: var(--ink); line-height: 1; }
  .tea-name__main { font-size: 24px; letter-spacing: 3px; }
  .tea-name__sub  { font-size: 16px; letter-spacing: 1.5px; margin-top: 3px; }

  .lid-content { position: absolute; inset: 0; transform: rotate(180deg); }

  .back-card {
    position: absolute; left: 47px; top: 44px; width: 376px; height: 372px; background: var(--ink);
  }
  .label-tab {
    position: absolute; left: 145px; top: 0; width: 180px; height: 100px;
    background: linear-gradient(90deg, var(--gold-c), var(--gold-b) 45%, var(--gold-a));
    padding: 0 9px 9px;
  }
  .label-tab__body { height: 100%; background: var(--ribbon); position: relative; }
  .label-tab .tea-name { top: 29px; }
  .label-tab .tea-name__main { font-size: 19px; letter-spacing: 2px; }
  .label-tab .tea-name__sub { font-size: 13px; letter-spacing: 1px; }

  .back-copy { position: absolute; left: 83px; top: 124px; width: 306px; color: var(--paper); font-size: 11.5px; line-height: 1.13; }
  .back-copy h2 { font-size: 11.5px; font-weight: 700; }
  .howto { position: absolute; left: 83px; top: 250px; color: var(--paper); }
  .howto h3 { font-size: 11px; font-weight: 700; margin-bottom: 7px; }
  .howto__icons { display: flex; gap: 15px; }
  .howto__icon {
    width: 53px; height: 53px; border: 2px solid var(--paper); border-radius: 9px;
    display: flex; flex-direction: column; align-items: center; justify-content: center;
    font-size: 7px; font-weight: 700; line-height: 1.05; text-align: center;
  }
  .howto__icon svg { width: 20px; height: 16px; margin-bottom: 3px; }
</style>
</head>
<body>

  <section class="panel panel--side">
    <div class="tile-area" role="img" aria-label="Repeating tile pattern built from the brand emblem, dark ornaments on kraft"></div>
  </section>

  <section class="panel panel--lid">
    <div class="ornament-faint" role="img" aria-label="Faint large ornamental emblem shape"></div>
    <div class="ribbon ribbon--full">
      <div class="ribbon__body">
        <div class="lid-content">
          <div class="brand-disc" style="top:133px"><span class="brand-name">Velka Brin</span></div>
          <div class="tea-name" style="top:297px">
            <div class="tea-name__main">CEYLON</div>
            <div class="tea-name__sub">BLACK TEA</div>
          </div>
        </div>
      </div>
    </div>
  </section>

  <section class="panel panel--back">
    <div class="ornament-frame" role="img" aria-label="Ornamental frame surrounding the information card"></div>
    <div class="back-card"></div>
    <div class="label-tab">
      <div class="label-tab__body">
        <div class="tea-name">
          <div class="tea-name__main">CEYLON</div>
          <div class="tea-name__sub">BLACK TEA</div>
        </div>
      </div>
    </div>
    <div class="back-copy">
      <h2>What's special about this tea?</h2>
      <p>Grown in the Fujian proince of China, tea buds are plucked within two hours of sprouting, then withered naturally in the sun. If your usual white tea appears green in your cup, then it is green tea; this, however, is the genuine article. Possibly one of our most exclusive teas - refreshing, light and aromatic.</p>
    </div>
    <div class="howto">
      <h3>How we like it:</h3>
      <div class="howto__icons">
        <div class="howto__icon">
          <svg viewBox="0 0 20 16" fill="none" stroke="#fff" stroke-width="1.6"><path d="M4 6h10v9H4z"/><path d="M9 6l5-5"/></svg>
          tea<br>1 per person
        </div>
        <div class="howto__icon">
          <svg viewBox="0 0 20 16" fill="none" stroke="#fff" stroke-width="1.6"><path d="M3 8a7 7 0 0 0 14 0z"/><path d="M8 4h4"/></svg>
          water<br>80°C
        </div>
        <div class="howto__icon">
          <svg viewBox="0 0 20 16" fill="none" stroke="#fff" stroke-width="1.6"><circle cx="6" cy="5" r="4"/><path d="M6 3v2h2"/><path d="M9 8h8v7H9z"/></svg>
          brew<br>3-5 minutes
        </div>
      </div>
    </div>
  </section>

  <section class="panel panel--front">
    <div class="ornament-dark" role="img" aria-label="Large dark ornamental emblem behind the ribbon"></div>
    <div class="ribbon ribbon--pointed">
      <div class="ribbon__body">
        <div class="brand-disc" style="top:40px"><span class="brand-name">Velka Brin</span></div>
        <div class="tea-name" style="top:198px">
          <div class="tea-name__main">CEYLON</div>
          <div class="tea-name__sub">BLACK TEA</div>
        </div>
      </div>
    </div>
  </section>

</body>
</html>
```